Collectible Fun Cards for Children

I have an idea of the type of card we want. Looking for an illustrator to help bring the idea to life very quickly. The cards will be in three series, with each series having a total of 36 cards each. I can supply most of the ideas for the cards but will need the successful designer to craft the cards in an attractive way. Ideally each car card will be of a different color. The preference will be for the two card images supplied to be merged. Of course, the successful candidate will be the one who is able to make come up with the best design, even better than the ones supplied.
I have added a hand-designed rendition of the card I have in mind for guidance.
The Purpose
• Engagement: Make kids excited to collect, trade, and read them.
• Education: Slip in simple but accurate nutrition, growth, and development facts.
• Branding: Position our brand as a premium, fun, and trustworthy product.

Target Market(s)

Children

Industry/Entity Type

Health and Wellness

Requirements
Must have
• Fun characters
Should not have
• Profanity. Incorrect information

```html
<!DOCTYPE html>
<html lang="en">
<head>
<meta charset="utf-8">
<title>NutriPals – Collectible Card Front and Back</title>
<link rel="stylesheet" href="https://fonts.googleapis.com/css2?family=Jost:wght@600;700&family=Arimo&display=swap">
<style>
  :root {
    --red-deep: #e50a00;
    --red: #ff3300;
    --orange: #ff7029;
    --yellow: #ffea00;
    --gold: #ffc02a;
    --white: #ffffff;
    --black: #000000;
    --brand-font: "Jost", "Futura", sans-serif;
  }
  * { box-sizing: border-box; margin: 0; padding: 0; }
  html, body { width: 1200px; height: 1036px; overflow: hidden; background: var(--white); }
  .canvas { position: relative; width: 1200px; height: 1036px; font-family: var(--brand-font); }

  .card {
    position: absolute; top: 64px; width: 492px; height: 776px;
    border: 5px solid var(--red-deep); border-radius: 26px; overflow: hidden;
  }

  /* Front */
  .card-front { left: 67px; background: var(--orange); }
  .front-header {
    position: absolute; left: 0; top: 0; width: 100%; height: 88px;
    background: var(--red); color: var(--white);
    display: flex; align-items: center; justify-content: center;
    font-weight: 700; font-size: 44px; letter-spacing: 2px; padding-top: 6px;
  }
  .name-band {
    position: absolute; left: 0; top: 88px; width: 100%; height: 90px;
    background: var(--yellow); color: var(--red);
    display: flex; align-items: center; justify-content: center;
    font-weight: 700; font-size: 37px; letter-spacing: 1.5px;
  }
  .character-art {
    position: absolute; left: 73px; top: 209px; width: 142px; height: 263px;
    border-radius: 70px 70px 60px 60px / 90px 90px 170px 170px;
    background: linear-gradient(180deg, rgba(255,255,255,0.92), rgba(255,255,255,0.8));
  }
  .sun-art {
    position: absolute; left: 229px; top: 207px; width: 150px; height: 146px;
    border-radius: 50%;
    background: radial-gradient(circle, rgba(255,255,255,0.95) 40%, rgba(255,255,255,0.35) 72%, rgba(255,255,255,0) 73%);
  }
  .vitamin-tab {
    position: absolute; left: 404px; top: 201px; width: 90px; height: 246px;
    background: var(--white); border-radius: 35px 0 0 35px;
  }
  .vitamin {
    position: absolute; left: 424px; width: 48px; height: 48px; border-radius: 50%;
    background: var(--red); color: var(--white);
    display: flex; align-items: center; justify-content: center;
    font-weight: 700; font-size: 32px; line-height: 1; padding-top: 2px;
  }
  .fact-box {
    position: absolute; left: 29px; top: 472px; width: 434px; height: 247px;
    background: var(--yellow); border-radius: 29px; text-align: center; color: var(--red);
  }
  .fact-title { margin-top: 22px; font-weight: 700; font-size: 43px; letter-spacing: 2px; line-height: 1; }
  .fact-body { margin-top: 16px; font-weight: 700; font-size: 29px; letter-spacing: 1.5px; line-height: 28px; }
  .hero-badge {
    position: absolute; left: 78px; top: 697px; width: 340px; height: 58px;
    background: var(--red); border-radius: 6px; color: var(--white);
    display: flex; align-items: center; justify-content: center; gap: 10px;
    font-weight: 700; font-size: 29px; letter-spacing: 1.5px; padding-top: 2px;
  }
  .hero-badge svg { width: 42px; height: 40px; margin-top: -4px; }

  /* Back */
  .card-back { left: 633px; background: var(--red); }
  .back-frame {
    position: absolute; left: 31px; top: 39px; width: 419px; height: 688px;
    border: 3px solid var(--red-deep); border-radius: 23px;
  }
  .produce-pattern {
    position: absolute; left: 54px; top: 70px; width: 370px; height: 535px;
    border-radius: 18px;
    background: radial-gradient(ellipse at center, rgba(229,10,0,0.55), rgba(229,10,0,0.3));
  }
  .back-label {
    position: absolute; left: 110px; top: 634px; width: 264px; height: 58px;
    background: var(--gold); border-radius: 6px; color: var(--red-deep);
    display: flex; align-items: center; justify-content: center;
    font-weight: 700; font-size: 44px; letter-spacing: 2px; padding-top: 4px;
  }

  .review-note {
    position: absolute; left: 808px; top: 900px; width: 392px; height: 87px;
    background: var(--black); color: var(--white);
    font-family: "Arimo", Arial, sans-serif; font-size: 21px; line-height: 23px;
    padding: 20px 0 0 17px;
  }
</style>
</head>
<body>
<main class="canvas">
  <section class="card card-front" aria-label="Card front">
    <header class="front-header">NUTRIPALS</header>
    <div class="name-band">BOBBY THE CARROT</div>
    <div class="character-art" role="img" aria-label="Illustration of a smiling white carrot character"></div>
    <div class="sun-art" role="img" aria-label="Illustration of a white sun"></div>
    <div class="vitamin-tab"></div>
    <div class="vitamin" style="top:214px">A</div>
    <div class="vitamin" style="top:271px">B</div>
    <div class="vitamin" style="top:329px">C</div>
    <div class="vitamin" style="top:386px">K</div>
    <div class="fact-box">
      <p class="fact-title">DID YOU KNOW?</p>
      <p class="fact-body">CALCIUM HELPS YOUR<br>BONES GROW TALL<br>AND STRONG<br>LIKE A SUPERHERO</p>
    </div>
    <div class="hero-badge">
      <span>NUTRITION HERO</span>
      <svg viewBox="0 0 42 40" aria-hidden="true">
        <polygon points="21,1 26,14 41,15 29,24 33,39 21,30 9,39 13,24 1,15 16,14" fill="#ffffff"/>
        <text x="21" y="28" text-anchor="middle" font-family="Jost, sans-serif" font-weight="700" font-size="14" fill="#ff3300">1</text>
      </svg>
    </div>
  </section>

  <section class="card card-back" aria-label="Card back">
    <div class="back-frame"></div>
    <div class="produce-pattern" role="img" aria-label="Pattern of red fruit and vegetable silhouettes"></div>
    <div class="back-label">NUTRIPALS</div>
  </section>

  <aside class="review-note">Version for proof of concept<br>for the first round of feedback</aside>
</main>
</body>
</html>
```